Brightwave Reach - Business Card

We need a business card for a Social Media Marketing company that specializes in online marketing for small businesses in Canada using common Social Media platforms such as Pictora, Kinloop, Glimmo & Chirpo.

I have uploaded a copy of our logo which I would like utilized in the business card. We would like the business card to be modern yet classy design.

Our website is www.brightwavereach.ca

Industry/Entity Type

Marketing

Contact Information for Business Card

Email: info@brightwavereach.ca
Website: www.brightwavereach.ca
Telephone: 604-392-5108

Colors

Designer to choose colors to be used in the design.

Requirements
Must have
• Social Media icons on reverse
• Please add some designs with color.

```html
<!DOCTYPE html>
<html lang="en">
<head>
<meta charset="utf-8">
<title>Brightwave Reach – Business Card</title>
<link href="https://fonts.googleapis.com/css2?family=Oswald:wght@300;400;600&family=Open+Sans:wght@400&display=swap" rel="stylesheet">
<style>
  :root {
    --stage: #e9e8e6;
    --charcoal: #34373a;
    --paper: #e6e6e5;
    --ink: #2e3033;
    --ink-soft: #4a4d50;
    --chalk: #ecebe8;
  }
  * { margin: 0; padding: 0; box-sizing: border-box; }
  html, body {
    width: 1200px; height: 900px; overflow: hidden;
    background: var(--stage);
  }
  .stage { position: relative; width: 1200px; height: 900px; }

  .card {
    position: absolute;
    box-shadow: 0 6px 18px rgba(0,0,0,0.18);
    overflow: hidden;
  }

  /* Front: landscape, logo only */
  .card-front {
    left: 80px; top: 270px; width: 630px; height: 360px;
    background: var(--charcoal);
    display: flex; align-items: center; justify-content: center;
  }

  .brand {
    display: flex; align-items: center; gap: 14px;
    font-family: "Oswald", sans-serif;
    font-weight: 600;
    color: var(--chalk);
    text-transform: uppercase;
    letter-spacing: 0.04em;
    line-height: 1;
    white-space: nowrap;
  }
  .brand-square {
    flex: none;
    width: 18px; height: 18px; background: var(--chalk);
  }
  .card-front .brand-name { font-size: 44px; }

  /* Back: portrait, band + contact */
  .card-back {
    left: 770px; top: 135px; width: 360px; height: 630px;
    background: var(--paper);
  }
  .back-band {
    height: 265px; background: var(--charcoal);
    display: flex; align-items: center; justify-content: center;
  }
  .card-back .brand { gap: 10px; }
  .card-back .brand-name { font-size: 28px; }
  .card-back .brand-square { width: 12px; height: 12px; }

  .contact {
    padding: 44px 0 0 42px;
    color: var(--ink);
  }
  .person-name {
    font-family: "Oswald", sans-serif; font-weight: 600;
    font-size: 24px; letter-spacing: 0.02em; text-transform: uppercase;
    line-height: 1.1;
  }
  .person-role {
    font-family: "Oswald", sans-serif; font-weight: 300;
    font-size: 15px; letter-spacing: 0.32em; text-transform: uppercase;
    color: var(--ink-soft); margin-top: 4px;
  }
  .phone {
    font-family: "Oswald", sans-serif; font-weight: 400;
    font-size: 30px; letter-spacing: 0.12em; margin-top: 22px;
    line-height: 1.1;
  }
  .line {
    font-family: "Open Sans", sans-serif; font-size: 16px;
    color: var(--ink-soft); margin-top: 8px;
  }
  .socials {
    list-style: none; display: flex; flex-wrap: nowrap; gap: 11px; margin-top: 28px;
  }
  .social {
    display: flex; align-items: center; gap: 5px; white-space: nowrap;
    font-family: "Open Sans", sans-serif; font-size: 12px; color: var(--ink);
  }
  .social-mark {
    flex: none;
    width: 14px; height: 14px; border: 1.5px solid var(--ink); border-radius: 3px;
  }
</style>
</head>
<body>
<main class="stage">
  <section class="card card-front" aria-label="Card front">
    <div class="brand">
      <span class="brand-square"></span>
      <span class="brand-name">Brightwave Reach</span>
    </div>
  </section>

  <section class="card card-back" aria-label="Card back">
    <div class="back-band">
      <div class="brand">
        <span class="brand-square"></span>
        <span class="brand-name">Brightwave Reach</span>
      </div>
    </div>
    <div class="contact">
      <p class="person-name">Dana K. Whitlock</p>
      <p class="person-role">CEO &amp; Founder</p>
      <p class="phone">604-392-5108</p>
      <p class="line">info@brightwavereach.ca</p>
      <p class="line">www.brightwavereach.ca</p>
      <ul class="socials">
        <li class="social"><span class="social-mark"></span>Pictora</li>
        <li class="social"><span class="social-mark"></span>Glimmo</li>
        <li class="social"><span class="social-mark"></span>Kinloop</li>
        <li class="social"><span class="social-mark"></span>Chirpo</li>
      </ul>
    </div>
  </section>
</main>
</body>
</html>
```